依頼詳細
A2の片面4色のポスターのデザインをお願いします。社内の掲示板等に掲示する予定です。健康的で楽しく、さわやかなイメージにするとともに、興味のない人の目を引くことができるようにしたいと思います。イラストではなく、写真を使用するイメージです。

参加しやすくなるように「もらなく参加賞がもらえる」「歩くだけでなくスポーツを歩数換算できる」点を伝えてください。
記載項目
タイトル・募集要項(キャンペーン概要)・健保名・キャッチ等

原稿データを添付いたします。
簡単なラフも添付しますが、ラフに縛られずに作業ください。
サイズ
A2
ページ数
片面
希望イメージ
シンプル 複雑
単色 カラフル
暗い 明るい
日常 高級
遊び心 厳粛
未来的 伝統的
女性的 男性的
希望する色
赤系、水色系、緑系
納品ファイル
補足説明

先方に提案したところ、当選案に決まりました。

皆様、素敵なご提案ありがとうございます。いただいたカンプに関して、他の健保様にも提案していこうと思います。別途ご相談する機会があるかもしれませんがその際はご協力いただければと思います。ありがとうございました。

```html
<!DOCTYPE html>
<html lang="ja">
<head>
<meta charset="utf-8">
<title>いきいきウォーキングキャンペーン 参加者募集</title>
<link rel="stylesheet" href="https://fonts.googleapis.com/css2?family=M+PLUS+Rounded+1c:wght@500;700;800;900&family=Noto+Sans+JP:wght@500;700;900&display=swap">
<style>
:root{
  --magenta:#e4207f;
  --magenta-dark:#c0105f;
  --yellow:#ffe83a;
  --green:#3cae48;
  --green-dark:#1f8a32;
  --sky:#bfe4f6;
  --sky-light:#d8eef9;
  --navy:#1c5ea8;
  --ink:#1c3f80;
  --gold:#d7a52a;
  --silver:#a6a6a6;
  --white:#ffffff;
}
*{margin:0;padding:0;box-sizing:border-box}
html,body{width:862px;height:1200px;overflow:hidden;background:var(--white)}
.poster{position:relative;width:862px;height:1200px;background:var(--white);font-family:"M PLUS Rounded 1c","Noto Sans JP",sans-serif;overflow:hidden}
.recruit-tab{position:absolute;left:262px;top:0;width:338px;height:52px;background:var(--magenta);color:var(--white);font-weight:900;font-size:30px;letter-spacing:20px;text-align:center;line-height:52px;padding-left:20px}
.badge{position:absolute;top:70px;width:222px;height:106px;border-radius:50%;background:var(--green);border:4px solid var(--white);box-shadow:0 0 0 2px var(--green);color:var(--white);font-weight:800;font-size:21px;line-height:1.35;text-align:center;display:flex;align-items:center;justify-content:center}
.badge--prize{left:32px}
.badge--sports{right:34px;top:72px}
.crown{position:absolute;left:98px;top:30px}
.sports-art{position:absolute;left:700px;top:42px;width:110px;height:40px;border-radius:20px;background:linear-gradient(90deg,#e8e8e8,#f3c9c9)}
.town-ring{position:absolute;left:52px;top:252px;width:740px;height:700px;border-radius:50%;background:radial-gradient(circle,transparent 0 46%,#eaf5c8 47%,#d3ebb0 56%,#eef7dc 64%,transparent 66%)}
.photo{position:absolute;left:186px;top:357px;width:472px;height:472px;border-radius:50%;background:linear-gradient(180deg,#3f8fd8 0%,#8cc3ee 45%,#e8eef4 80%,#f4f4f4 100%);border:3px solid #c9de5a}
.title{position:absolute;left:0;top:0}
.catch{position:absolute;left:40px;top:638px;width:34px;writing-mode:vertical-rl;color:var(--magenta);font-weight:900;font-size:23px;line-height:34px;white-space:nowrap}
.catch-arrow{position:absolute;left:84px;top:822px}
.merit{position:absolute;top:812px;width:200px;height:184px}
.merit__tab{position:absolute;left:0;top:0;width:80px;height:172px;border-radius:12px;background:linear-gradient(180deg,var(--sky-light),var(--sky));border:2px solid #9ed2ee}
.merit__tab span{position:absolute;left:8px;top:10px;writing-mode:vertical-rl;color:var(--ink);font-weight:900;font-size:25px;line-height:28px;white-space:nowrap}
.merit__body{position:absolute;left:46px;top:42px;width:150px;height:142px;border-radius:14px;background:var(--green);border:2px solid var(--white);box-shadow:0 0 0 1px var(--green-dark);color:var(--white);text-align:center;padding-top:12px}
.merit__head{color:var(--yellow);font-weight:900;font-size:19px;line-height:1.1;margin-bottom:8px}
.merit__text{font-weight:700;font-size:12.5px;line-height:1.55}
.merit--1{left:122px}
.merit--2{left:366px}
.merit--3{left:610px}
.merit--2 .merit__head{font-size:17px}
.details{position:absolute;left:0;top:1013px;width:862px;height:152px;background:var(--sky)}
.details__left{position:absolute;left:46px;top:18px;width:390px;color:var(--ink);font-weight:700;font-size:12.5px;line-height:1.6}
.row{display:flex;align-items:center;margin-top:3px}
.label{display:inline-block;width:78px;height:18px;border-radius:9px;background:var(--navy);color:var(--white);font-size:11.5px;line-height:18px;text-align:center;margin-right:10px;flex:none}
.date{color:var(--magenta);font-weight:900;font-size:21px;line-height:1.1;white-space:nowrap}
.date small{font-size:14px}
.details__right{position:absolute;left:444px;top:10px;width:400px;color:var(--ink);font-weight:700;font-size:11.5px;line-height:1.55}
.apply{display:flex}
.apply .label{width:62px;margin-top:2px}
.prizes{display:flex;align-items:center;margin-top:12px;white-space:nowrap}
.prizes .label{width:62px}
.prize{display:inline-flex;align-items:center;font-size:12px;font-weight:800;margin-right:10px;white-space:nowrap}
.prize__mark{display:inline-block;width:56px;height:20px;border-radius:4px;color:var(--white);font-size:12px;text-align:center;line-height:20px;margin-right:3px}
.prize--gold .prize__mark{background:var(--gold)}
.prize--silver .prize__mark{background:var(--silver)}
.footer{position:absolute;left:0;top:1167px;width:862px;height:33px;background:var(--navy);color:var(--white);font-weight:800;font-size:19px;text-align:center;line-height:33px;letter-spacing:1px}
</style>
</head>
<body>
<div class="poster">
  <div class="recruit-tab">参加者募集</div>

  <svg class="crown" width="48" height="34" viewBox="0 0 48 34" aria-hidden="true">
    <path d="M3 10 L13 20 L24 4 L35 20 L45 10 L41 28 L7 28 Z" fill="#e8b73a" stroke="#b88514" stroke-width="2"/>
    <rect x="7" y="28" width="34" height="5" fill="#d29a1e"/>
  </svg>
  <div class="badge badge--prize">もれなく<br>賞品を進呈</div>

  <div class="sports-art" role="img" aria-label="スポーツ用品のイラスト(ボール・シャトル・旗)"></div>
  <div class="badge badge--sports">各種スポーツも<br>歩数換算 OK</div>

  <div class="town-ring" role="img" aria-label="木や家、車、風船が円を描く町並みのイラスト"></div>
  <div class="photo" role="img" aria-label="青空の下を笑顔でウォーキングする男女の写真"></div>

  <svg class="title" width="862" height="470" viewBox="0 0 862 470">
    <defs>
      <linearGradient id="lively" x1="0" x2="1">
        <stop offset="0" stop-color="#f7a21c"/>
        <stop offset="1" stop-color="#e4207f"/>
      </linearGradient>
      <path id="titleArc" d="M62 440 Q 430 30 800 440"/>
    </defs>
    <text x="324" y="128" font-family="'M PLUS Rounded 1c',sans-serif" font-weight="900" font-size="50" fill="url(#lively)">い<tspan font-size="34">き</tspan>い<tspan font-size="34">き</tspan></text>
    <text font-family="'M PLUS Rounded 1c',sans-serif" font-weight="900" font-size="76" fill="#e4207f" stroke="#ffe83a" stroke-width="7" paint-order="stroke" stroke-linejoin="round" text-anchor="middle">
      <textPath href="#titleArc" startOffset="50%" textLength="860" lengthAdjust="spacingAndGlyphs">ウォーキングキャンペーン</textPath>
    </text>
  </svg>

  <div class="catch">歩くってこんなに良いことが!</div>
  <svg class="catch-arrow" width="22" height="46" viewBox="0 0 22 46" aria-hidden="true">
    <path d="M0 0 L22 23 L0 46 Z" fill="#f08ab8"/>
  </svg>

  <div class="merit merit--1">
    <div class="merit__tab"><span>気分爽快!</span></div>
    <div class="merit__body">
      <div class="merit__head">リフレッシュ</div>
      <p class="merit__text">歩くことで<br>運動だけでなく<br>気分転換も<br>できます。</p>
    </div>
  </div>
  <div class="merit merit--2">
    <div class="merit__tab"><span>老化予防!</span></div>
    <div class="merit__body">
      <div class="merit__head">アンチ<br>エイジング</div>
      <p class="merit__text">年齢に伴う<br>筋力低下や<br>骨粗しょう症を<br>予防できます。</p>
    </div>
  </div>
  <div class="merit merit--3">
    <div class="merit__tab"><span>脂肪燃焼!</span></div>
    <div class="merit__body">
      <div class="merit__head">アンチメタボ</div>
      <p class="merit__text">内臓脂肪の燃焼で<br>メタボリック<br>シンドロームを<br>解消できます。</p>
    </div>
  </div>

  <section class="details">
    <div class="details__left">
      <p>1日平均1万歩以上、2ヵ月で60万歩以上を目標に、<br>歩くことや各種スポーツを通じて健康づくりに取り組みます。</p>
      <div class="row"><span class="label">対象者</span>○○○○健康保険組合の被保険者</div>
      <div class="row"><span class="label">募集期間</span><span class="date">8月21日<small>(水)</small>〜 9月10日<small>(火)</small></span></div>
      <div class="row"><span class="label">取組期間</span><span class="date">10月 1日<small>(火)</small>〜11月30日<small>(土)</small></span></div>
    </div>
    <div class="details__right">
      <div class="apply"><span class="label">申込方法</span><p>所定の「参加申込書」必要事項を記入し、捺印のうえ、人事担当課に提出します。申込者には「万歩計」と「記録カード」を配布しますので、毎日の歩数と歩数換算するスポーツを記録し、期間終了後に合算して人事担当課に提出してください。</p></div>
      <div class="prizes">
        <span class="label">賞品</span>
        <span class="prize prize--gold"><span class="prize__mark">達成賞</span>(60万歩以上)</span>
        <span class="prize prize--silver"><span class="prize__mark">努力賞</span>(42万歩以上)</span>
      </div>
    </div>
  </section>

  <footer class="footer">○○○○健康保険組合</footer>
</div>
</body>
</html>
```